its a new company based in Christchurch new Zealand building computers ,repairs, upgrades and anything computers for the general public,i like bright happy colours like yellows, greens reds anything that stands out and it needs to communicant trust and security towards my new company,i have no logo yet,

Target Market(s)

target market of all ages

Industry/Entity Type

Building

Contact Information for Business Card

Pixel Harbour Limited,ph-0274829315,email-brightnode47@mailvista.example,14c tamworth cl,kelvale

```html
<!DOCTYPE html>
<html lang="en">
<head>
<meta charset="utf-8">
<title>Pixel Harbour Limited – Business Card</title>
<link rel="stylesheet" href="https://fonts.googleapis.com/css2?family=Open+Sans:wght@400;700&display=swap">
<style>
  :root {
    --backdrop: #e4e4e4;
    --card: #ffffff;
    --wave-red: #e2362b;
    --wave-orange: #f57c1f;
    --wave-yellow: #f9c21a;
    --stripe-green: #2eaa4a;
    --brand: #1f8a3b;
    --accent: #d9302a;
    --ink: #2f2f2f;
    --ink-soft: #555555;
  }
  * { margin: 0; padding: 0; box-sizing: border-box; }
  html, body {
    width: 1200px;
    height: 900px;
    overflow: hidden;
    background: var(--backdrop);
    font-family: "Open Sans", Arial, sans-serif;
  }
  .card {
    position: absolute;
    left: 100px;
    top: 164px;
    width: 1000px;
    height: 572px;
    background: var(--card);
    overflow: hidden;
    box-shadow: 0 14px 40px rgba(0,0,0,0.18);
  }
  .card__wave {
    position: absolute;
    inset: 0;
    width: 100%;
    height: 100%;
  }
  .wave__band { fill: url(#waveFill); }
  .wave__stripe { fill: var(--stripe-green); }
  .brand {
    position: absolute;
    left: 110px;
    top: 258px;
    display: flex;
    align-items: center;
    gap: 14px;
  }
  .brand__mark {
    width: 30px;
    height: 30px;
    background: var(--brand);
  }
  .brand__name {
    font-size: 30px;
    font-weight: 700;
    color: var(--brand);
  }
  .contact {
    position: absolute;
    left: 250px;
    bottom: 40px;
    font-size: 25px;
    line-height: 1.32;
    color: var(--ink);
    font-style: normal;
  }
  .person {
    position: absolute;
    right: 50px;
    top: 222px;
    text-align: right;
  }
  .person__name {
    font-size: 30px;
    font-weight: 700;
    color: var(--accent);
    line-height: 1.2;
  }
  .person__role {
    font-size: 27px;
    color: var(--ink-soft);
    line-height: 1.2;
    margin-bottom: 28px;
  }
  .person__line {
    font-size: 25px;
    color: var(--ink);
    line-height: 1.32;
  }
</style>
</head>
<body>
  <section class="card" aria-label="Pixel Harbour Limited business card">
    <svg class="card__wave" viewBox="0 0 1000 572" preserveAspectRatio="none" aria-hidden="true">
      <defs>
        <linearGradient id="waveFill" x1="0" y1="0" x2="1" y2="0">
          <stop offset="0" stop-color="#e2362b"/>
          <stop offset="0.55" stop-color="#f57c1f"/>
          <stop offset="1" stop-color="#f9c21a"/>
        </linearGradient>
      </defs>
      <path class="wave__band" d="M0,0 H1000 V150 C860,150 760,60 600,80 C420,104 300,200 0,160 Z"/>
      <path class="wave__stripe" d="M0,186 C300,228 430,126 610,104 C770,86 870,172 1000,176 V192 C870,190 770,104 610,122 C440,142 300,248 0,204 Z"/>
    </svg>

    <div class="brand">
      <span class="brand__mark"></span>
      <span class="brand__name">Pixel Harbour Limited</span>
    </div>

    <address class="contact">
      <div>14c tamworth cl,</div>
      <div>kelvale</div>
      <div>Email: brightnode47@mailvista.example</div>
      <div>Website: www.pixelharbour.example</div>
    </address>

    <div class="person">
      <div class="person__name">Maren Ostby-Hale</div>
      <div class="person__role">Consultant</div>
      <div class="person__line">Fax: 027 482 9315</div>
      <div class="person__line">Phone: 027 482 9315</div>
    </div>
  </section>
</body>
</html>
```